Make an Awesome Graphic for a PPT

Attached is the specific content for the project. the X-factor of Adoption. It does not need a title just take the existing graphic an improve it. Attached is our company logo for color palette and the "ugly version". It should look modern and edge in terms of effect and font. Need it by Monday March 7th

```html
<!DOCTYPE html>
<html lang="en">
<head>
<meta charset="utf-8">
<title>The X-Factor of Adoption</title>
<link rel="stylesheet" href="https://fonts.googleapis.com/css2?family=Exo+2:wght@600;700;800&display=swap">
<style>
  :root {
    --blue-deep: #1a3f95;
    --blue-bright: #0a7cc9;
    --grey-dark: #7f828f;
    --grey-light: #c8cad0;
    --grey-mid: #8e9099;
    --label: #ffffff;
    --title: #1c4da0;
    --paper: #ffffff;
  }
  html, body {
    margin: 0;
    padding: 0;
    width: 1200px;
    height: 761px;
    overflow: hidden;
    background: var(--paper);
  }
  .canvas {
    display: block;
    width: 1200px;
    height: 761px;
  }
  .segment-label {
    font-family: "Exo 2", sans-serif;
    font-weight: 600;
    font-size: 17px;
    letter-spacing: 0.5px;
    fill: var(--label);
  }
  .zone-title {
    font-family: "Exo 2", sans-serif;
    font-weight: 800;
    font-size: 40px;
    letter-spacing: 1.5px;
    fill: var(--title);
  }
  .brand-name {
    font-family: "Exo 2", sans-serif;
    font-weight: 800;
    font-size: 46px;
    letter-spacing: 1px;
    fill: var(--blue-deep);
  }
</style>
</head>
<body>
<svg class="canvas" viewBox="0 0 1200 761" xmlns="http://www.w3.org/2000/svg" aria-label="The X-factor of adoption diagram">
  <defs>
    <linearGradient id="blue-band" x1="0" y1="0" x2="1" y2="0">
      <stop offset="0" stop-color="var(--blue-deep)"/>
      <stop offset="1" stop-color="var(--blue-bright)"/>
    </linearGradient>
    <linearGradient id="grey-band" x1="0" y1="0" x2="1" y2="0">
      <stop offset="0" stop-color="var(--grey-dark)"/>
      <stop offset="1" stop-color="var(--grey-light)"/>
    </linearGradient>
  </defs>

  <g class="x-mark">
    <!-- Innovation concept, upper right -->
    <path class="arm arm-innovation-top" fill="url(#grey-band)"
          d="M688,140 L935,140 L738,340 L686,340 L852,196 L720,196 L660,248 L620,214 Z"/>
    <!-- Farmer experience, upper left -->
    <path class="arm arm-experience" fill="url(#blue-band)"
          d="M265,140 L512,140 L672,318 L628,340 L470,196 L386,196 L490,310 L490,340 L432,340 Z"/>
    <!-- Innovation concept, lower left -->
    <path class="arm arm-innovation-bottom" fill="url(#grey-band)"
          d="M240,620 L495,620 L580,500 L545,475 L470,565 L350,565 L520,422 L468,422 Z"/>
    <!-- Farmer sentiment, lower right -->
    <path class="arm arm-sentiment" fill="url(#blue-band)"
          d="M528,422 L584,422 L708,565 L855,565 L712,422 L762,422 L960,620 L700,620 Z"/>

    <polygon class="notch notch-top" fill="var(--grey-light)" points="502,336 541,293 580,336"/>
    <polygon class="notch notch-bottom" fill="var(--grey-mid)" points="630,426 680,426 655,449"/>
  </g>

  <g class="segment-labels">
    <text class="segment-label" x="318" y="166">FARMER</text>
    <text class="segment-label" x="318" y="187">EXPERIENCE</text>

    <text class="segment-label" x="750" y="166">INNOVATION</text>
    <text class="segment-label" x="772" y="187">CONCEPT</text>

    <text class="segment-label" x="336" y="589">INNOVATION</text>
    <text class="segment-label" x="318" y="610">CONCEPT</text>

    <text class="segment-label" x="775" y="589">FARMER</text>
    <text class="segment-label" x="760" y="610">SENTIMENT</text>
  </g>

  <g class="zone">
    <text class="zone-title" x="600" y="376" text-anchor="middle">ADOPTION</text>
    <text class="zone-title" x="600" y="412" text-anchor="middle">ZONE</text>
  </g>

  <text class="brand-name" x="1165" y="718" text-anchor="end">FIELDROOT</text>
</svg>
</body>
</html>
```